Halden & Pruitt Periodontics and Implant Solutions Business Card

We are a specialty dental practice- implants and periodontal surgery. We have just re-designed our logo and are building a new office and would like to re-design our business card. We are looking for something professional with a creative and artsy twist- something to stand out among the rest! Happy Designing!

I have uploaded all versions of our new logo and our current business card. We have 3 locations and 2 doctors.

Target Market(s)

55+

Industry/Entity Type

Dental

Contact Information for Business Card

Needs Names, logo, locations- professional and artsy!

Colors
0555a3
0592cd
34a7d7
3277b5
85cae6
85acd3
cee9f5
ecf7fb

Requirements
Must have
• our names:
• Thomas E. Halden D.M.D.
• Celia M. Pruitt D.M.D.
• Diplomate of the National Council of Gum Surgery
• Address locations:
• 462 W. Larkspur Avenue Suite 210B Plantation, FL 33871
• Tel: 954-318-2264 Fax: 954-318-2291
• 5127 Harlow Lane #C-4 Boca Raton, FL 33609
• Tel: 561-627-1958 Fax: 561-703-2816
• 274 Northwest 9th Street #412 Miami FL 33987
• Tel: 786-429-6153 Fax: 786-429-6170
Nice to have
• unique look
Should not have
• doesn't need QR like our current card has.

```html
<!DOCTYPE html>
<html lang="en">
<head>
<meta charset="utf-8">
<title>Halden &amp; Pruitt Business Card</title>
<link href="https://fonts.googleapis.com/css2?family=Open+Sans:wght@400;600;700&display=swap" rel="stylesheet">
<style>
  :root{
    --navy:#2d2a70;
    --white:#ffffff;
    --backdrop:#262626;
    --icon-grey:#c9c9d6;
  }
  *{box-sizing:border-box;margin:0;padding:0}
  html,body{width:966px;height:1200px;overflow:hidden;background:var(--backdrop);font-family:"Open Sans",sans-serif}
  .sheet{position:relative;width:966px;height:1200px}
  .card{position:absolute;top:230px;width:440px;height:740px;background:var(--white);overflow:hidden}
  .card--front{left:30px}
  .card--back{left:496px}

  .brand{position:absolute;left:0;right:0;top:0;display:flex;align-items:center;justify-content:center;gap:14px;padding:0 34px;color:var(--navy)}
  .card--front .brand{height:300px}
  .card--back .brand{height:270px}
  .brand__dot{width:54px;height:54px;border-radius:50%;background:var(--navy);flex:none}
  .brand__name{font-weight:600;font-size:18px;line-height:1.35;white-space:nowrap}

  .panel{position:absolute;left:0;right:0;background:var(--navy);color:var(--white)}
  .card--front .panel{top:300px;height:412px}
  .card--back .panel{top:270px;height:442px}

  .credential{text-align:center;padding-top:36px;font-size:19px;line-height:1.5}
  .credential strong{font-weight:700;display:block}

  .rule{position:absolute;left:0;right:0;height:7px;background:var(--white)}
  .badge{position:absolute;left:38px;width:44px;height:44px;background:var(--white);transform:rotate(45deg)}
  .badge svg{position:absolute;left:9px;top:9px;width:26px;height:26px;transform:rotate(-45deg)}
  .doctor{position:absolute;left:110px;font-size:19px}
  .web{position:absolute;left:110px;font-size:18px;line-height:1.45}

  .locations-title{text-align:center;padding-top:28px;font-weight:700;font-size:20px}
  .office{position:absolute;left:20px;right:14px;font-size:16px;line-height:1.5}
  .office__row{display:flex;align-items:flex-start;gap:12px}
  .office__row svg{flex:none;width:16px;height:16px;margin-top:4px}
  .office__city{font-weight:700;padding-left:28px}
  .bottom-strip{position:absolute;left:0;right:0;bottom:0;height:28px;background:var(--white)}
</style>
</head>
<body>
<div class="sheet">

  <section class="card card--front">
    <header class="brand">
      <span class="brand__dot"></span>
      <span class="brand__name">Halden &amp; Pruitt<br>Periodontics and Implant Solutions</span>
    </header>
    <div class="panel">
      <p class="credential"><strong>DIPLOMATE OF THE NATIONAL</strong>COUNCIL OF GUM SURGERY</p>

      <div class="rule" style="top:150px"></div>
      <div class="badge" style="top:131px"><svg viewBox="0 0 26 26"><circle cx="13" cy="9" r="5.5" fill="var(--navy)"/><path d="M3 25c0-6 4.5-9 10-9s10 3 10 9z" fill="var(--navy)"/></svg></div>
      <p class="doctor" style="top:192px">Thomas E. Halden D.M.D.</p>

      <div class="rule" style="top:240px"></div>
      <div class="badge" style="top:221px"><svg viewBox="0 0 26 26"><circle cx="13" cy="9" r="5.5" fill="var(--navy)"/><path d="M3 25c0-6 4.5-9 10-9s10 3 10 9z" fill="var(--navy)"/></svg></div>
      <p class="doctor" style="top:282px">Celia M. Pruitt D.M.D.</p>

      <div class="rule" style="top:330px"></div>
      <div class="badge" style="top:311px"><svg viewBox="0 0 26 26" fill="none" stroke="var(--navy)" stroke-width="1.8"><circle cx="13" cy="13" r="10"/><ellipse cx="13" cy="13" rx="4.5" ry="10"/><path d="M3 13h20M5 8h16M5 18h16"/></svg></div>
      <p class="web" style="top:356px">www.haldenperio.com<br>contactus@haldenperio.com</p>
    </div>
    <div class="bottom-strip"></div>
  </section>

  <section class="card card--back">
    <header class="brand">
      <span class="brand__dot"></span>
      <span class="brand__name">Halden &amp; Pruitt<br>Periodontics and Implant Solutions</span>
    </header>
    <div class="panel">
      <h2 class="locations-title">ADDRESS LOCATIONS</h2>

      <div class="office" style="top:72px">
        <div class="office__row"><svg viewBox="0 0 16 16"><path d="M3 1h3l1.5 4-2 1.3a9 9 0 0 0 4.2 4.2L11 8.5l4 1.5v3c0 1-1 2-2 2C7 15 1 9 1 3c0-1 1-2 2-2z" fill="var(--icon-grey)"/></svg><span>Tel: 954-318-2264 Fax: 954-318-2291</span></div>
        <div class="office__row"><svg viewBox="0 0 16 16"><path d="M8 1a5 5 0 0 1 5 5c0 4-5 9-5 9S3 10 3 6a5 5 0 0 1 5-5z" fill="var(--icon-grey)"/><circle cx="8" cy="6" r="2" fill="var(--navy)"/></svg><span>462 W. Larkspur Avenue Suite 210B</span></div>
        <div class="office__city">Plantation, FL 33871</div>
      </div>
      <div class="rule" style="top:178px"></div>

      <div class="office" style="top:200px">
        <div class="office__row"><svg viewBox="0 0 16 16"><path d="M3 1h3l1.5 4-2 1.3a9 9 0 0 0 4.2 4.2L11 8.5l4 1.5v3c0 1-1 2-2 2C7 15 1 9 1 3c0-1 1-2 2-2z" fill="var(--icon-grey)"/></svg><span>Tel: 561-627-1958 Fax: 561-703-2816</span></div>
        <div class="office__row"><svg viewBox="0 0 16 16"><path d="M8 1a5 5 0 0 1 5 5c0 4-5 9-5 9S3 10 3 6a5 5 0 0 1 5-5z" fill="var(--icon-grey)"/><circle cx="8" cy="6" r="2" fill="var(--navy)"/></svg><span>5127 Harlow Lane #C-4</span></div>
        <div class="office__city">Boca Raton, FL 33609</div>
      </div>
      <div class="rule" style="top:306px"></div>

      <div class="office" style="top:328px">
        <div class="office__row"><svg viewBox="0 0 16 16"><path d="M3 1h3l1.5 4-2 1.3a9 9 0 0 0 4.2 4.2L11 8.5l4 1.5v3c0 1-1 2-2 2C7 15 1 9 1 3c0-1 1-2 2-2z" fill="var(--icon-grey)"/></svg><span>Tel: 786-429-6153 Fax: 786-429-6170</span></div>
        <div class="office__row"><svg viewBox="0 0 16 16"><path d="M8 1a5 5 0 0 1 5 5c0 4-5 9-5 9S3 10 3 6a5 5 0 0 1 5-5z" fill="var(--icon-grey)"/><circle cx="8" cy="6" r="2" fill="var(--navy)"/></svg><span>274 Northwest 9th Street #412</span></div>
        <div class="office__city">Miami FL 33987</div>
      </div>
    </div>
    <div class="bottom-strip"></div>
  </section>

</div>
</body>
</html>
```